New website

We ned to create a new website that reflects more who we are. We are delivering exclusive premium products to our customers and the current website does not reflect our products at all.
We believe in less is more and need a webpage that is clean yet professional and exclusive.

Target Market(s)

Dentistry

Industry/Entity Type

Dental

Number of Pages Required

5+ page

Font styles to use
Sans Serif

Colors

Designer to choose colors to be used in the design.

Requirements
Must have
• Picture gallery
• Nice structure
• Clean layout
Nice to have
• Light fonts
Should not have
• Any italic font styles

```html
<!DOCTYPE html>
<html lang="en">
<head>
<meta charset="utf-8">
<title>Lumadent — About</title>
<link href="https://fonts.googleapis.com/css2?family=Montserrat:wght@400;600;700&family=Open+Sans:wght@300;400&display=swap" rel="stylesheet">
<style>
:root{
  --cyan:#4fc6df;
  --red:#e24a4a;
  --ink:#2f2f2f;
  --muted:#8a8a8a;
  --footer:#0a3a46;
  --footer-text:#6f8f97;
  --track:#ececec;
}
*{margin:0;padding:0;box-sizing:border-box}
html,body{width:894px;height:1200px;overflow:hidden;background:#fff}
body{position:relative;font-family:"Open Sans",sans-serif;color:var(--ink);font-style:normal}
.abs{position:absolute}

/* header */
.site-header{left:0;top:0;width:894px;height:42px;background:#fff}
.brand{left:174px;top:11px;display:flex;align-items:center;gap:7px;font-family:"Montserrat",sans-serif;font-weight:700;font-size:12px;color:#333;letter-spacing:.3px}
.brand-dot{width:14px;height:14px;border-radius:50%;background:var(--cyan)}
.nav{top:16px;font-family:"Montserrat",sans-serif;font-weight:600;font-size:6.4px;color:#333;letter-spacing:.2px}
.nav.active{color:var(--cyan)}

/* page title band */
.title-band{left:0;top:42px;width:894px;height:59px;background:linear-gradient(90deg,#5ccce3,#58c9e1 50%,#62cfe5)}
.title-band h1{position:absolute;top:17px;width:100%;text-align:center;font-family:"Montserrat",sans-serif;font-weight:700;font-size:11px;color:#fff;letter-spacing:.3px}
.crumbs{position:absolute;top:34px;width:100%;text-align:center;font-size:6px;color:#e8f8fc}

/* about */
.about-frame{left:189px;top:174px;width:232px;height:306px;border:3px solid var(--cyan)}
.about-photo{left:207px;top:157px;width:233px;height:305px;background:linear-gradient(160deg,#3aa8bf 0%,#5b8f9c 30%,#a58570 50%,#d9dde0 75%,#bfc9cd 100%)}
.plus{font-family:"Montserrat",sans-serif;font-weight:700;color:var(--cyan);line-height:1}
.about-title{left:468px;top:187px;font-family:"Montserrat",sans-serif;font-weight:700;font-size:10.5px;letter-spacing:.3px}
.rule{height:1.5px;width:32px;background:var(--cyan)}
.about-text{left:468px;top:222px;width:254px;font-size:6.3px;line-height:12.6px;color:var(--muted);font-weight:300}
.skill{left:468px;width:252px}
.skill-label{display:flex;justify-content:space-between;font-family:"Montserrat",sans-serif;font-weight:600;font-size:6.2px;color:#333}
.skill-track{margin-top:4px;height:3px;background:var(--track)}
.skill-fill{height:3px;background-image:repeating-linear-gradient(90deg,transparent 0 24px,#fff 24px 25px),linear-gradient(90deg,#e24a4a,#9a7f93 50%,#4fc6df);background-size:auto,100% 3px}
.btn{background:var(--cyan);color:#fff;font-family:"Montserrat",sans-serif;font-weight:700;font-size:5.6px;display:flex;align-items:center;justify-content:center;letter-spacing:.2px}

/* call band */
.call-band{left:0;top:518px;width:894px;height:174px;background:linear-gradient(100deg,#58c8e0,#63cfe6 50%,#52c4dd)}
.call-card{left:174px;top:546px;width:546px;height:118px;background:#fff}
.call-frame{left:194px;top:565px;width:507px;height:79px;border:2px solid var(--cyan)}
.call-title{left:174px;top:582px;width:546px;text-align:center;font-size:11px;color:#555;font-weight:300}
.call-phone{left:174px;top:598px;width:546px;text-align:center;font-size:19px;color:var(--red)}

/* testimonials */
.section-title{left:0;top:745px;width:894px;text-align:center;font-family:"Montserrat",sans-serif;font-weight:700;font-size:10.5px;letter-spacing:.3px}
.avatar-frame{width:38px;height:38px;border:1.5px solid var(--cyan)}
.avatar{width:38px;height:38px}
.quote{width:160px;text-align:center;font-size:6.1px;line-height:12.6px;color:var(--muted);font-weight:300}
.person{width:160px;text-align:center;font-family:"Montserrat",sans-serif;font-weight:700;font-size:6.2px}
.sign{width:38px;height:14px;background:linear-gradient(90deg,#d6f1f7,#bfe8f2)}

/* footer */
.site-footer{left:0;top:995px;width:894px;height:162px;background:var(--footer)}
.foot-brand{left:174px;top:1028px;display:flex;align-items:center;gap:7px;font-family:"Montserrat",sans-serif;font-weight:700;font-size:12px;color:#fff}
.foot-text{font-size:6.1px;line-height:12.6px;color:var(--footer-text);font-weight:300}
.foot-head{font-family:"Montserrat",sans-serif;font-weight:700;font-size:5.8px;color:#fff;top:1033px}
.foot-rule{top:1043px;width:16px;height:1.5px;background:var(--cyan)}
.info{display:flex;align-items:center;gap:6px;font-size:6.1px;color:var(--footer-text)}
.social{top:1105px;width:5px;height:5px;border-radius:50%;background:#4c7e89}
.gallery{left:594px;top:1059px;width:127px;display:grid;grid-template-columns:repeat(4,29px);grid-auto-rows:29px;gap:3px 3.6px}
.gallery-item{display:block;border:1px solid #ffffff22}
.copyright{left:0;top:1172px;width:894px;text-align:center;font-size:6.6px;color:#888}
.copyright b{color:#333;font-weight:600}
</style>
</head>
<body>

<header class="abs site-header">
  <div class="abs brand"><span class="brand-dot"></span>LUMADENT</div>
  <span class="abs nav active" style="left:408px">HOME</span>
  <span class="abs nav" style="left:446px">PAGES</span>
  <span class="abs nav" style="left:486px">SERVICES</span>
  <span class="abs nav" style="left:536px">GALLERY</span>
  <span class="abs nav" style="left:584px">BLOG</span>
  <span class="abs nav" style="left:620px">CONTACTS</span>
  <span class="abs nav" style="left:673px">APPOINTMENT</span>
</header>

<section class="abs title-band">
  <h1>ABOUT</h1>
  <div class="crumbs">Home &nbsp;/&nbsp; Pages &nbsp;/&nbsp; About</div>
</section>

<!-- about -->
<div class="abs about-frame"></div>
<div class="abs plus" style="left:163px;top:167px;font-size:20px">+</div>
<div class="abs about-photo" role="img" aria-label="Close-up of a dentist wearing a blue surgical cap and white face mask"></div>

<h2 class="abs about-title">WE ARE LUMADENT</h2>
<div class="abs rule" style="left:468px;top:206px"></div>
<p class="abs about-text">Dentures actually improve our smiles and overall apperance. Not only they make us look better, but also make our life easier. Enjoy simple things as food, conversation and smile. Forget about uncomfortable social encounters. Our focus is on your overall well being and helping you achieve optimal health and esthetics.</p>

<div class="abs skill" style="top:286px">
  <div class="skill-label"><span>DENTAL PREVENTION</span><span>75%</span></div>
  <div class="skill-track"><div class="skill-fill" style="width:75%"></div></div>
</div>
<div class="abs skill" style="top:318px">
  <div class="skill-label"><span>FLUORIDE TREATMENT</span><span>50%</span></div>
  <div class="skill-track"><div class="skill-fill" style="width:50%"></div></div>
</div>
<div class="abs skill" style="top:349px">
  <div class="skill-label"><span>TOOTH EXTRACTION</span><span>90%</span></div>
  <div class="skill-track"><div class="skill-fill" style="width:90%"></div></div>
</div>
<div class="abs skill" style="top:381px">
  <div class="skill-label"><span>CAVITY FILLING</span><span>85%</span></div>
  <div class="skill-track"><div class="skill-fill" style="width:85%"></div></div>
</div>
<a class="abs btn" style="left:468px;top:414px;width:82px;height:18px">LEARN ABOUT US</a>

<!-- call to action -->
<section class="abs call-band"></section>
<div class="abs call-card"></div>
<div class="abs call-frame"></div>
<div class="abs" style="left:435px;top:560px;width:24px;height:10px;background:#fff"></div>
<div class="abs" style="left:442px;top:559px;width:10px;height:10px;border-radius:50%;background:var(--cyan)"></div>
<p class="abs call-title">Dentistry For People Who Love To Smile</p>
<p class="abs call-phone">+ 0 (800) 555 01 23</p>
<div class="abs" style="left:388px;top:640px;width:118px;height:8px;background:#fff"></div>
<a class="abs btn" style="left:394px;top:635px;width:106px;height:18px">MAKE AN APPOINTMENT</a>

<!-- testimonials -->
<h2 class="abs section-title">WHAT OUR PATIENTS SAY</h2>
<div class="abs rule" style="left:431px;top:765px"></div>

<div class="abs avatar-frame" style="left:238px;top:808px"></div>
<div class="abs plus" style="left:224px;top:802px;font-size:13px">+</div>
<div class="abs avatar" style="left:242px;top:803px;background:linear-gradient(160deg,#e8d6b8,#c9b8a6)" role="img" aria-label="Portrait of a smiling blonde woman"></div>
<p class="abs quote" style="left:181px;top:860px">"Boudin jerky short ribs occaecat, labore ad consectetur velit ex ground round tenderloin. Deserunt tongue sunt pork belly velit leberkas"</p>
<p class="abs person" style="left:181px;top:911px">CLARA HENSLEY</p>
<div class="abs sign" style="left:242px;top:923px" role="img" aria-label="Handwritten signature"></div>

<div class="abs avatar-frame" style="left:424px;top:808px"></div>
<div class="abs plus" style="left:410px;top:802px;font-size:13px">+</div>
<div class="abs avatar" style="left:428px;top:803px;background:linear-gradient(160deg,#dcdcdc,#8aa0b5)" role="img" aria-label="Portrait of a smiling man in a suit"></div>
<p class="abs quote" style="left:367px;top:860px">"Pork chop drumstick eiusmod, short ribs short loin boudin ground round pork loin in ham hock excepteur occaecat chuck esse labore"</p>
<p class="abs person" style="left:367px;top:911px">OMAR VELDEN</p>
<div class="abs sign" style="left:428px;top:923px" role="img" aria-label="Handwritten signature"></div>

<div class="abs avatar-frame" style="left:610px;top:808px"></div>
<div class="abs plus" style="left:596px;top:802px;font-size:13px">+</div>
<div class="abs avatar" style="left:614px;top:803px;background:linear-gradient(160deg,#f0f0f0,#5a5f6a)" role="img" aria-label="Portrait of a bearded man in a dark suit"></div>
<p class="abs quote" style="left:553px;top:860px">"Esse duis in ut, ea pork chop aute ut tempor cupidatat. Tempor bresaola do et beef tail. In reprehenderit kevin ad jerky anim flank velit turkey officia"</p>
<p class="abs person" style="left:553px;top:911px">PETER MARSH</p>
<div class="abs sign" style="left:614px;top:923px" role="img" aria-label="Handwritten signature"></div>

<!-- footer -->
<footer class="abs site-footer"></footer>
<div class="abs foot-brand"><span class="brand-dot"></span>LUMADENT</div>
<p class="abs foot-text" style="left:174px;top:1054px;width:128px">Sausage nulla velit, spare ribs picanha jerky ball tip pork chop turkey ut id beef ribs kielbasa capicola.</p>
<span class="abs social" style="left:175px"></span>
<span class="abs social" style="left:188px"></span>
<span class="abs social" style="left:204px"></span>
<span class="abs social" style="left:218px"></span>

<p class="abs foot-head" style="left:314px">CONTACT INFO</p>
<div class="abs foot-rule" style="left:314px"></div>
<div class="abs info" style="left:314px;top:1057px">
  <svg width="7" height="8" viewBox="0 0 7 8"><path d="M3.5 0a3 3 0 0 0-3 3c0 2.2 3 5 3 5s3-2.8 3-5a3 3 0 0 0-3-3z" fill="#4fc6df"/><circle cx="3.5" cy="3" r="1.1" fill="#0a3a46"/></svg>14 Harbor Lane, Westfield</div>
<div class="abs info" style="left:314px;top:1080px">
  <svg width="8" height="8" viewBox="0 0 8 8"><circle cx="4" cy="4" r="3.2" fill="none" stroke="#4fc6df" stroke-width="1.2"/><path d="M4 2v2.2h1.6" fill="none" stroke="#4fc6df" stroke-width="1"/></svg>09:00 - 22:00</div>
<div class="abs info" style="left:314px;top:1103px">
  <svg width="8" height="8" viewBox="0 0 8 8"><path d="M1.6.5l1.4 1.6-.8 1a4.5 4.5 0 0 0 1.9 1.9l1-.8L6.8 5.6 6 7.2C3.2 7 1 4.8.8 2z" fill="#4fc6df"/></svg>0 (800) 555 01 23</div>

<p class="abs foot-head" style="left:454px">TESTIMONIALS</p>
<div class="abs foot-rule" style="left:454px"></div>
<p class="abs foot-text" style="left:454px;top:1054px;width:128px">"Pork chop drumstick eiusmod, short ribs short loin boudin ground round pork loin in ham hock excepteur occaecat"</p>
<div class="abs" style="left:454px;top:1096px;width:40px;height:14px;background:linear-gradient(90deg,#1d5966,#2a6e7c)" role="img" aria-label="Handwritten signature"></div>

<p class="abs foot-head" style="left:594px">OUR WORKS</p>
<div class="abs foot-rule" style="left:594px"></div>
<nav class="abs gallery" aria-label="Picture gallery of our works">
  <a class="gallery-item" style="background:#cfd9d8" role="img" aria-label="Smiling patient"></a>
  <a class="gallery-item" style="background:#c5dde4" role="img" aria-label="Dental team"></a>
  <a class="gallery-item" style="background:#a9d4e0" role="img" aria-label="Dentist in scrubs"></a>
  <a class="gallery-item" style="background:#d3e6ea" role="img" aria-label="Dental staff"></a>
  <a class="gallery-item" style="background:#bcdbe2" role="img" aria-label="Dental team at work"></a>
  <a class="gallery-item" style="background:#d9dfe2" role="img" aria-label="Patient smiling"></a>
  <a class="gallery-item" style="background:#e3e9ec" role="img" aria-label="Doctor portrait"></a>
  <a class="gallery-item" style="background:#b8dbe3" role="img" aria-label="Dental staff group"></a>
</nav>

<p class="abs copyright">© 2016 Lumadent. Created with <span style="color:var(--cyan)">♡</span> by <b>Northline Studio</b></p>

</body>
</html>
```